Redesign Login page

I want to redesign my login page to bring my 2 products closer together. I am only looking to redesign one login page, not 2.

For the logo, please make it solid and it can be black or white if helpful. I can also fine tune the logo if you get it close.

Coding

Coded - Design and coding required

Number of Pages Required

1 page

```html
<!DOCTYPE html>
<html lang="en">
<head>
<meta charset="utf-8">
<title>Northvale — Sign In</title>
<link rel="stylesheet" href="https://fonts.googleapis.com/css2?family=Saira:wght@400;500;600;700&family=Outfit:wght@400;500&display=swap">
<style>
  :root {
    --page-bg: #012d2c;
    --card-bg: #ffffff;
    --ink: #111111;
    --muted: #6b6b6b;
    --line: #d9d9d9;
    --brand-red: #8e1309;
    --brand-gold: #917b26;
    --pill-grey: #eeeeee;
    --footer-bg: #44625f;
    --footer-ink: #ffffff;
  }
  * { box-sizing: border-box; margin: 0; padding: 0; }
  html, body { width: 1200px; height: 588px; overflow: hidden; }
  body {
    position: relative;
    background: var(--page-bg);
    font-family: "Saira", sans-serif;
    color: var(--ink);
  }
  .login-card {
    position: absolute;
    left: 406px; top: 66px;
    width: 388px; height: 431px;
    background: var(--card-bg);
  }
  .welcome {
    position: absolute; top: 26px; left: 0; width: 100%;
    text-align: center; font-size: 13px; font-weight: 500; letter-spacing: 0.3px;
  }
  .brand-name {
    position: absolute; top: 48px; left: 0; width: 100%;
    text-align: center; font-size: 30px; font-weight: 700;
    color: var(--brand-red); letter-spacing: 0.5px;
  }
  .field-label {
    position: absolute; left: 54px;
    font-size: 10px; color: var(--muted); letter-spacing: 0.3px;
  }
  .field {
    position: absolute; left: 54px;
    width: 281px; height: 37px;
    border: 1px solid var(--line); border-radius: 4px;
    display: flex; align-items: center;
  }
  .field-icon {
    width: 26px; height: 26px; border-radius: 50%;
    background: var(--brand-red);
    margin-left: 6px; margin-right: 8px;
    display: flex; align-items: center; justify-content: center;
    flex: none;
  }
  .field-placeholder { font-size: 10px; color: var(--muted); letter-spacing: 0.3px; flex: 1; }
  .field-toggle { margin-right: 8px; display: flex; }
  .options {
    position: absolute; left: 54px; top: 251px; width: 281px;
    display: flex; align-items: center; justify-content: space-between;
    font-size: 10px; letter-spacing: 0.3px;
  }
  .remember { display: flex; align-items: center; color: var(--muted); }
  .checkbox {
    width: 16px; height: 16px; border: 1px solid var(--line); border-radius: 3px;
    margin-right: 6px;
  }
  .link { color: var(--brand-red); text-decoration: underline; }
  .submit {
    position: absolute; left: 100px; top: 280px;
    width: 188px; height: 34px; border-radius: 5px;
    background: var(--brand-gold); color: #fff;
    font-size: 11.5px; font-weight: 600; letter-spacing: 0.3px;
    display: flex; align-items: center; justify-content: center;
  }
  .alt-login {
    position: absolute; top: 338px; left: 108px;
    height: 36px; display: flex; align-items: center;
  }
  .alt-pill {
    position: relative; height: 36px; width: 92px;
    background: var(--pill-grey); border-radius: 18px;
    display: flex; align-items: center;
    font-size: 10px; color: var(--muted); letter-spacing: 0.3px;
    padding-left: 32px;
  }
  .or-badge {
    position: absolute; left: 0; top: 6px;
    width: 24px; height: 24px; border-radius: 50%;
    background: var(--page-bg); color: #fff;
    font-size: 10px; font-weight: 600;
    display: flex; align-items: center; justify-content: center;
  }
  .provider {
    width: 35px; height: 35px; border-radius: 50%;
    background: var(--pill-grey); margin-left: 3px;
    display: flex; align-items: center; justify-content: center;
  }
  .provider-mark { width: 12px; height: 12px; border-radius: 50%; background: var(--muted); }
  .provider-mark.square { border-radius: 1px; }
  .signup {
    position: absolute; top: 395px; left: 0; width: 100%;
    text-align: center; font-size: 10px; color: var(--muted); letter-spacing: 0.3px;
  }
  .site-footer {
    position: absolute; left: 0; top: 554px;
    width: 1200px; height: 34px;
    background: var(--footer-bg); color: var(--footer-ink);
    font-family: "Outfit", sans-serif;
  }
  .copyright { position: absolute; left: 155px; top: 9px; font-size: 11.5px; }
  .contact { font-size: 10px; margin-left: 6px; text-decoration: underline; }
  .social { position: absolute; left: 962px; top: 5px; display: flex; align-items: center; }
  .social-icon {
    width: 10px; height: 10px; background: var(--footer-ink); border-radius: 1px;
    margin: 0 9px;
  }
  .social-round {
    width: 24px; height: 24px; border-radius: 50%;
    background: var(--page-bg); margin-left: 8px;
    display: flex; align-items: center; justify-content: center;
  }
  .social-round span { width: 8px; height: 8px; border-radius: 50%; background: var(--footer-ink); }
</style>
</head>
<body>
  <main class="login-card">
    <p class="welcome">Welcome to</p>
    <h1 class="brand-name">Northvale</h1>

    <label class="field-label" style="top:124px">Username</label>
    <div class="field" style="top:138px">
      <span class="field-icon">
        <svg width="14" height="14" viewBox="0 0 14 14" fill="none" stroke="#fff" stroke-width="1.1">
          <circle cx="7" cy="4.5" r="2.7"/>
          <path d="M2.2 13c0-3 2.2-4.8 4.8-4.8s4.8 1.8 4.8 4.8z"/>
        </svg>
      </span>
      <span class="field-placeholder">Enter your username</span>
    </div>

    <label class="field-label" style="top:186px">Password</label>
    <div class="field" style="top:201px">
      <span class="field-icon">
        <svg width="14" height="14" viewBox="0 0 14 14" fill="none" stroke="#fff" stroke-width="1.2">
          <rect x="2.5" y="6" width="9" height="7"/>
          <path d="M4.5 6V4a2.5 2.5 0 0 1 5 0v2"/>
        </svg>
      </span>
      <span class="field-placeholder">Enter your password</span>
      <span class="field-toggle">
        <svg width="16" height="10" viewBox="0 0 16 10" fill="none" stroke="#888" stroke-width="1">
          <path d="M1 5c2-3 4.3-4 7-4s5 1 7 4c-2 3-4.3 4-7 4S3 8 1 5z"/>
          <circle cx="8" cy="5" r="1.6" fill="#888"/>
        </svg>
      </span>
    </div>

    <div class="options">
      <span class="remember"><span class="checkbox"></span>Remember Me</span>
      <span class="link">Forgot Password?</span>
    </div>

    <div class="submit">Submit</div>

    <div class="alt-login">
      <div class="alt-pill"><span class="or-badge">or</span>Login With</div>
      <div class="provider" role="img" aria-label="Login with Keyline"><span class="provider-mark"></span></div>
      <div class="provider" role="img" aria-label="Login with Quadra"><span class="provider-mark square"></span></div>
    </div>

    <p class="signup">Don't Have An Account? <span class="link">Sign Up</span></p>
  </main>

  <footer class="site-footer">
    <p class="copyright">© 2025 Northvale. All Rights Reserved. <span class="contact">Contact Us</span></p>
    <div class="social">
      <span class="social-icon" role="img" aria-label="Linkora"></span>
      <span class="social-icon" role="img" aria-label="Snapwell"></span>
      <span class="social-round" role="img" aria-label="Chirper"><span></span></span>
    </div>
  </footer>
</body>
</html>
```